Business Card Design

My company is a health food catering and delivery business. Our colours are a bright turquiose green/blue, black, white and natural brown based beige. I would like the front of my card (working from the outside in; with a turquoise green boarder -quite thick, with a thin black line separating the turquoise boarder from the beige inside the remaining space of the front of the card with my logo in the centre. This should be all that appears on the front.

On the back I would like all the information displayed above on the beige coloured card, with the blurb in the bright turquoise and my contact information in black please. I would like my business name central - Harvest Lantern Kitchen and immediately below with a right alignment - ...Dine with Delight
Below this should follow all that I have displayed above with a left alignment.

Target Market(s)

Cafes, restaurants, individuals, buying agents & super markets

Industry/Entity Type

Catering

Contact Information for Business Card

BACK OF BUSINESS CARD:
Harvest Lantern Kitchen
...Dine with Delight
Deliciously healthy foods - free from gluten, lactose, cane sugar, trans-fat, GMO corn, soy & rice, no artificial flavours, colours or preservatives.
Prepared fresh from locally sourced ingredients, delivered to your door! For individuals, families, corporate, cafes, restaurants & event catering for Toowoomba & surrounds!

PH: 0491 382 907 // orders@harvestlanternkitchen.example
www.harvestlanternkitchen.example
www.social.example/harvestlanternkitchen

Requirements
Must have
• Please supply a modern, easy to read text that will blend nicely with my logo text.
Nice to have
• I really want my business cards to stand out as these will be the template for brochures, menus and website designers to draw inspiration from!
Should not have
• Please do not use Arial, Tahoma or Times Roman text.

```html
<!DOCTYPE html>
<html lang="en">
<head>
<meta charset="utf-8">
<title>Harvest Lantern Kitchen – Business Card</title>
<link rel="stylesheet" href="https://fonts.googleapis.com/css2?family=Open+Sans:wght@300;400&display=swap">
<style>
  :root {
    --turquoise: #83c5bd;
    --beige: #ecdec4;
    --ink: #2b2b2b;
    --rule: #3a4a48;
    --page: #ffffff;
    --frame: #b9b9b9;
    --art: #d9c9ab;
  }
  * { margin: 0; padding: 0; box-sizing: border-box; }
  html, body { width: 1200px; height: 391px; overflow: hidden; background: var(--page); }
  body { font-family: "Open Sans", sans-serif; color: var(--ink); }

  .sheet {
    position: relative;
    width: 1200px; height: 391px;
    border: 1px solid var(--frame);
  }

  .card {
    position: absolute;
    top: 32px;
    width: 526px; height: 324px;
    background: var(--beige);
    overflow: hidden;
  }
  .card--front { left: 65px; }
  .card--back { left: 610px; }

  .band {
    position: absolute; left: 0; right: 0;
    background: var(--turquoise);
  }
  .card--front .band--top { top: 0; height: 36px; border-bottom: 1px solid var(--ink); }
  .card--front .band--bottom { bottom: 0; height: 34px; border-top: 1px solid var(--ink); }

  .logo-art {
    position: absolute;
    left: 112px; top: 52px;
    width: 290px; height: 178px;
    background: radial-gradient(ellipse at center, var(--art) 0%, var(--beige) 78%);
    border-radius: 12px;
  }
  .logo-name {
    position: absolute;
    left: 0; right: 0; top: 238px;
    text-align: center;
    font-size: 30px;
    font-weight: 400;
    color: var(--ink);
  }

  .card--back .band--header {
    top: 0; height: 117px;
    border-bottom: 1px solid var(--rule);
  }
  .brand-name {
    position: absolute; left: 0; right: 0; top: 52px;
    text-align: center;
    font-size: 32px; font-weight: 300;
    color: var(--beige);
    line-height: 1;
  }
  .tagline {
    position: absolute; right: 96px; top: 91px;
    font-size: 13px; color: var(--ink);
    line-height: 1;
  }

  .blurb {
    position: absolute; left: 40px; right: 40px; top: 124px;
    text-align: center;
    font-size: 11.6px; line-height: 17px;
  }
  .blurb p + p { margin-top: 6px; }

  .contact {
    position: absolute; left: 0; right: 0; top: 256px;
    text-align: center;
    font-size: 11.6px; line-height: 17px;
  }
  .contact .social { font-size: 9.6px; margin-top: 6px; }
</style>
</head>
<body>
  <div class="sheet">
    <section class="card card--front">
      <div class="band band--top"></div>
      <div class="logo-art" role="img" aria-label="Line illustration of a chef in a toque holding a whisk and a frying pan"></div>
      <div class="logo-name">Harvest Lantern Kitchen</div>
      <div class="band band--bottom"></div>
    </section>

    <section class="card card--back">
      <header class="band band--header">
        <h1 class="brand-name">Harvest Lantern Kitchen</h1>
        <p class="tagline">...Dine with Delight</p>
      </header>
      <div class="blurb">
        <p>Deliciously healthy foods - free from gluten, lactose, cane sugar, trans-fat,<br>GMO corn, soy &amp; rice, no artificial flavours, colours or preservatives.</p>
        <p>Prepared fresh from locally sourced ingredients, delivered to your door!</p>
        <p>For individuals, families, corporate, cafes, restaurants &amp; event<br>catering for Toowoomba &amp; surrounds!</p>
      </div>
      <div class="contact">
        <p>PH: 0491 382 907 | orders@harvestlanternkitchen.example</p>
        <p>www.harvestlanternkitchen.example</p>
        <p class="social">www.social.example/harvestlanternkitchen</p>
      </div>
    </section>
  </div>
</body>
</html>
```